gka 2014 bcard design

We have a new logo that we have yet to incorporate into any of our materials. We are under the gun to get new business cards done as soon as possible. This is our 20th year in business and we specialize in providing entertainment and audio-visual services for private and corporate events. Please see our website for more www.goldkiteacts.com
Being that we're in the entertainment industry, our "look" can be somewhat edgy and risky, but at the same time not "over the top". In fact, we would probably lean to a "less is more" style.
One side of the card should have our contact information for phones, email and address, and the other should have our slogan "Gather, Inspire, Delight". We also want Facebook and Instagram (goldkiteactsevents) there as well, but not sure if it should be on back or front.
Target Market(s)
High net worth individuals, creative types in both the corporate and social markets
Industry/Entity Type
Entertainment
Look and feel

```html
<!DOCTYPE html>
<html lang="en">
<head>
<meta charset="utf-8">
<title>gold kite acts — business cards</title>
<link rel="stylesheet" href="https://fonts.googleapis.com/css2?family=Comfortaa:wght@400&family=Josefin+Sans:wght@400&family=Oswald:wght@500&family=Tinos:wght@700&display=swap">
<style>
  :root {
    --page: #e6e4e0;
    --ink: #0b0b0b;
    --paper: #f7f7f5;
    --white: #ffffff;
    --slogan: #c9c9c9;
    --muted: #8a8a8a;
    --brand-blue: #1f7fd6;
    --social-mark: #3c4a5c;
  }
  * { box-sizing: border-box; margin: 0; padding: 0; }
  html, body { width: 1200px; height: 1023px; overflow: hidden; }
  body {
    background: var(--page);
    position: relative;
    font-family: "Josefin Sans", sans-serif;
  }
  .card {
    position: absolute;
    left: 220px;
    width: 760px;
    height: 434px;
    overflow: hidden;
    box-shadow: 0 6px 18px rgba(0,0,0,.18);
  }

  /* Front: slogan side */
  .card--slogan { top: 58px; background: var(--ink); }
  .card--slogan .brand-dot {
    position: absolute; left: -150px; top: 90px;
    width: 380px; height: 380px; border-radius: 50%;
    background: var(--brand-blue);
  }
  .card--slogan .identity { position: absolute; left: 300px; top: 92px; }
  .wordmark {
    font-family: "Comfortaa", sans-serif;
    font-weight: 400;
    letter-spacing: -1px;
    line-height: 1;
    white-space: nowrap;
  }
  .card--slogan .wordmark { color: var(--white); font-size: 54px; }
  .descriptor {
    text-transform: uppercase;
    letter-spacing: 5px;
    line-height: 1;
    white-space: nowrap;
  }
  .card--slogan .descriptor { color: var(--white); font-size: 24px; margin-top: 14px; }
  .slogan {
    font-family: "Oswald", sans-serif;
    font-weight: 500;
    color: var(--slogan);
    font-size: 31px;
    text-transform: uppercase;
    letter-spacing: 1px;
    margin-top: 22px;
    white-space: nowrap;
  }
  .social {
    position: absolute; right: 34px; bottom: 30px;
    display: flex; align-items: center; gap: 10px;
    color: var(--muted); font-size: 18px;
  }
  .social .mark {
    width: 22px; height: 22px; border-radius: 4px; background: var(--social-mark);
  }

  /* Back: contact side */
  .card--contact {
    top: 532px;
    background: var(--paper);
    border: 12px solid var(--ink);
  }
  .rule { position: absolute; left: 0; right: 0; height: 3px; background: var(--ink); }
  .rule--top { top: 42px; }
  .rule--bottom { bottom: 62px; }
  .card--contact .identity {
    position: absolute; left: 38px; top: 82px;
    display: flex; align-items: center; gap: 22px;
  }
  .card--contact .brand-dot {
    width: 104px; height: 104px; border-radius: 50%;
    background: var(--brand-blue);
  }
  .card--contact .wordmark { color: var(--ink); font-size: 50px; }
  .card--contact .descriptor { color: #333; font-size: 22px; margin-top: 10px; }
  .contact {
    position: absolute; left: 0; right: 0; top: 222px;
    text-align: center;
    font-family: "Tinos", serif;
    font-weight: 700;
    font-size: 19px;
    line-height: 1.35;
    color: var(--ink);
    list-style: none;
  }
</style>
</head>
<body>
  <section class="card card--slogan" aria-label="Card front with slogan">
    <div class="brand-dot"></div>
    <div class="identity">
      <p class="wordmark">gold kite acts</p>
      <p class="descriptor">Events &amp; Entertainment</p>
      <p class="slogan">Gather, Inspire, Delight</p>
    </div>
    <div class="social">
      <span class="mark"></span>
      <span class="handle">goldkiteactsevents</span>
    </div>
  </section>

  <section class="card card--contact" aria-label="Card back with contact details">
    <div class="rule rule--top"></div>
    <div class="identity">
      <div class="brand-dot"></div>
      <div>
        <p class="wordmark">gold kite acts</p>
        <p class="descriptor">Events &amp; Entertainment</p>
      </div>
    </div>
    <ul class="contact">
      <li>Tel : +1 212-555-0148</li>
      <li>Email : info@goldkiteacts.com</li>
      <li>Website : www.goldkiteacts.com</li>
      <li>48 Harbor Lane, 3rd Floor New York, NY 10014</li>
    </ul>
    <div class="rule rule--bottom"></div>
  </section>
</body>
</html>
```